Dentistry Office

We want a new design for a Dentist's office website.

The theme is: "We provide high quality, state-of-the-art, dental care in a comfortable, caring environment."

The site currently has a menu on the left of the page with about 40 items on it. There is a great deal of textual content on each page, plus several illustrations.

We want to do this using CSS, so we need specifications in the CSS for all possible elements. The CSS needs to be named in a logical manner for easy use.

Every dentist on the planet seems to use lots of Flash. We don't want to because it is so distracting. We are looking for an elegant solution targeting 24-55 age group, but not excluding anyone.

The following (from another dentist's site) can give you a taste of what we want to communicate on the site:

"After 20 years of teaching dentists how to refine their technique and many years of writing textbooks, I currently devote my time to my office and the hands-on practice of dentistry. I'd like to welcome you personally to my dental practice, and I invite you to meet my highly experienced team of professionals.

"We have offered complete dental care of the highest quality since 1978. We provide Preventive Services, Tooth Whitening and Cosmetic Dentistry for a beautiful smile, Endodontics (root canal treatment) to treat painful teeth, Sedation Dentistry so you can relax, and Dental Implants to restore what is missing. We offer total care.

"Our approach to your health is simple: We use our education, experience and dedication to provide every patient with superior dental care.

"This passion for excellence is not just a goal, but a standard every member of our team holds.

"We also pride ourselves with our state of the art procedures, training and technology. This includes creating a beautiful smile using techniques that preserve as much of the original tooth as possible.

"Our abilities are renowned throughout the dental profession and I hope if you have any questions you will contact us by an e-mail note, by phone or just by dropping by."

Keep in mind the screen shape and dimensions. Your design needs to work in the normal screen proportions, regardless of how it looks when you post it here. Scrolling is OK, but the first impression needs to work.

Keep in mind that there will be about 250 words, or more, on each page.

Competitors web sites:

http://www.brevalkoortho.example/

http://www.quimbelfieldcare.example/

http://www.grinsatdoverellclinic.example/

http://www.trunwickfamilydentalcare.example/

http://www.morvanhaledental.example/

http://www.ubrigandental.example/

We need to compete with these.

Target Market(s)

Generally adults seeking the most experienced and comfortable-to-be-with dentist.

Industry/Entity Type

Training

Requirements
Must have
• Must stand apart from other dentists.
• Must be elegant.
• Must have a horizontal menu structure across all columns, NOT a vertical that requires scrolling, no popout, pop down, etc. menus.
• We are looking for something special.
• Do not waste your time or ours putting up templates and things you have used before.
• Personally, I do not see how someone outside the US can understand the northern California dental market. But you are welcome to try.
Should not have
• Flash or graphics that move
• The look of a template
• Folksy fonts
• Looks like you used it 20 times before

```html
<!DOCTYPE html>
<html lang="en">
<head>
<meta charset="utf-8">
<title>Alder Crest Dentist – Martin Kellgren</title>
<link href="https://fonts.googleapis.com/css2?family=Arimo:ital,wght@0,400;0,700;1,400;1,700&family=PT+Sans:wght@400;700&display=swap" rel="stylesheet">
<style>
:root{
  --teal:#19a8cc;
  --blue:#2f9fd2;
  --blue-light:#6fc3e7;
  --ink:#111;
  --grey:#8a8a8a;
  --grey-dark:#6f6f6f;
  --rule:#c9d3d8;
  --page:#ffffff;
  --backdrop:#b9b9b9;
  --nav:#000;
}
*{margin:0;padding:0;box-sizing:border-box}
html,body{width:923px;height:1200px;overflow:hidden}
body{background:linear-gradient(90deg,#a9a9a9 0,#d6d6d6 40.6px,#d6d6d6 879px,#a9a9a9 923px);font-family:Arimo,Arial,sans-serif;color:var(--ink)}
.site{position:relative;width:923px;height:1200px}
.sheet{position:absolute;left:40.6px;top:0;width:839px;height:1200px;background:var(--page)}
.abs{position:absolute}

/* header */
.header{left:40.6px;top:0;width:839px;height:212px;background:linear-gradient(180deg,#fff 0,#fff 30px,#eeeeee 30px,#fafafa 170px,#fff 212px)}
.brand{left:64px;top:2px;font-family:"PT Sans",Arial,sans-serif;font-size:27px;color:var(--teal);letter-spacing:.2px;line-height:30px}
.doctor{left:64px;top:30px;font-family:"PT Sans",Arial,sans-serif;font-size:27px;color:var(--grey-dark);line-height:30px}
.tagline{left:64px;top:86px;font-family:"PT Sans",Arial,sans-serif;font-size:12.2px;line-height:16.5px;color:var(--grey-dark)}
.hero-photo{left:420px;top:30px;width:459.6px;height:182px;background:radial-gradient(ellipse at 45% 50%,#e7c5a8 0,#d9ab8a 25%,#8a6a55 45%,#f0e8df 75%,#f5f5f5 100%)}

/* topic menu */
.topics{left:40.6px;top:222px;width:839px;height:160px}
.topic{position:absolute;top:0}
.topic h3{font-family:Arimo,Arial,sans-serif;font-weight:400;font-size:13px;color:var(--teal);line-height:18px;margin-bottom:3px}
.topic li{list-style:none;font-size:10.2px;line-height:12.9px;color:var(--grey)}
.topic-rule{position:absolute;top:2px;width:1px;height:95px;background:#ddd}

/* nav */
.nav{left:40.6px;top:388px;width:839px;height:24.5px;background:var(--nav)}
.nav a{position:absolute;top:0;line-height:24.5px;color:#fff;font-size:10.3px;font-weight:700;text-decoration:none;letter-spacing:.1px}

/* location band */
.office-photo{left:40.6px;top:412.5px;width:167px;height:133px;background:linear-gradient(180deg,#7d8c66 0,#6a5a4c 45%,#8c8a86 70%,#bdbdb8 100%)}
.band{left:208px;top:412.5px;width:671.6px;height:133px;background:linear-gradient(90deg,#2f9bcf 0,#4eaedc 45%,#3aa2d3 75%,#2f98cc 100%);color:#fff;padding:12px 0 0 12.5px;font-size:10.8px;line-height:14.8px}
.band strong{display:block;margin-bottom:15px}
.band p{margin-bottom:14.8px;width:640px}

/* left rail */
.promo{left:40.6px;top:545.5px;width:167.4px;height:197.5px;background:linear-gradient(180deg,#dff2fb 0,#e9f6fc 40%,#cfeaf7 100%);padding:50px 0 0 13.5px}
.promo h4{font-size:14.6px;line-height:18.6px;color:var(--blue);font-weight:700}
.promo p{margin-top:15px;font-size:8.6px;line-height:11.5px;color:var(--ink);padding-left:0}
.rail-rule{left:208px;top:545.5px;width:1px;height:654.5px;background:#d8d8d8}
.rail{left:54.5px;width:150px}
.rail-title{font-size:13.4px;color:var(--blue);line-height:18px}
.hours{top:773px}
.hours b{display:block;font-size:9.8px;margin-top:9px;line-height:14.8px}
.hours li{list-style:none;font-size:9.8px;line-height:14.8px}
.map{top:913px}
.stay{top:943px}
.contact{top:1063px;font-size:11.2px;line-height:14.8px;color:var(--blue)}
.contact strong{font-size:12.7px}

/* main */
.main{left:230px;width:640px}
.section-title{font-size:13.4px;color:var(--blue);line-height:18px}
.provides{top:561px}
.services{margin-top:9px}
.services li{list-style:none;position:relative;padding-left:13px;font-size:10.6px;line-height:14.8px}
.services li::before{content:"✱";position:absolute;left:-1px;top:0;color:var(--blue);font-size:9px}
.divider{left:208px;top:742.5px;width:669px;height:0;border-top:1px dashed #8aa7b4}
.commitment{top:773px}
.letter{margin-top:10px;font-size:10.6px;line-height:14.8px}
.letter p{margin-bottom:14.8px}
.letter .motto{color:var(--blue);font-style:italic;font-weight:700}
</style>
</head>
<body>
<div class="site">
  <div class="abs sheet"></div>

  <header class="abs header"></header>
  <div class="abs brand">ALDER CREST DENTIST</div>
  <div class="abs doctor">Martin Kellgren</div>
  <p class="abs tagline">Providing Cosmetic Dentistry Excellence to Patients in Santa Rosa,<br>Sonoma County and the San Francisco Bay Area.</p>
  <div class="abs hero-photo" role="img" aria-label="Photo of two smiling young women"></div>

  <nav class="abs topics">
    <div class="topic" style="left:24px">
      <h3>EDUCATION</h3>
      <ul><li>Emergency Dental Care</li><li>Your Mouth</li><li>Your Tooth</li><li>Cracked Tooth?</li><li>Missing a Tooth?</li><li>Sensitive Teeth</li><li>Dry Mouth</li><li>Tooth Grinding</li><li>Sleep Dentistry</li><li>Videos</li></ul>
    </div>
    <span class="topic-rule" style="left:168px"></span>
    <div class="topic" style="left:186px">
      <h3>PREVENTATIVE</h3>
      <ul><li>What is Preventive Care?</li><li>Taking Care of Your Teeth</li><li>Eating Right</li><li>Dental Check-Ups</li><li>Sealants</li><li>Periodontal Disease</li><li>Kicking the Habit</li><li>Night Guards</li><li>Dental X-Rays</li><li>Antibiotics with Treatment</li></ul>
    </div>
    <span class="topic-rule" style="left:335px"></span>
    <div class="topic" style="left:350px">
      <h3>COSMETICS</h3>
      <ul><li>Cosmetic Dentistry</li><li>Bleaching and Whitening</li><li>Cosmetic Bonding</li><li>Esthetic Veneers</li><li>Tooth Shaping</li></ul>
    </div>
    <span class="topic-rule" style="left:503px"></span>
    <div class="topic" style="left:519.5px">
      <h3>RESTORATIONS</h3>
      <ul><li>Crowns/Caps: Each Step</li><li>CMBRs</li><li>Porcelain Bridges</li><li>Bonded Dental Bridges</li><li>Gold Restorations</li><li>Implants</li><li>Treating Cracked Teeth</li><li>Periodontal (gum) Treatment</li></ul>
    </div>
    <span class="topic-rule" style="left:672px"></span>
    <div class="topic" style="left:687.5px">
      <h3>VISITING OUR OFFICE</h3>
      <ul><li>Where to Stay</li><li>First Visit / Map</li><li>Financial Policy</li><li>Dental Insurance</li></ul>
    </div>
  </nav>

  <nav class="abs nav">
    <a href="#" style="left:24px">HOME</a>
    <a href="#" style="left:105px">WHY WE ARE DIFFERENT</a>
    <a href="#" style="left:272.5px">TECHNOLOGIES WE OFFER</a>
    <a href="#" style="left:451.5px">MEET DR. KELLGREN</a>
    <a href="#" style="left:591.5px">OUR STAFF</a>
    <a href="#" style="left:696px">CONTACT US / LINKS</a>
  </nav>

  <div class="abs office-photo" role="img" aria-label="Photo of the dental office building among trees"></div>
  <section class="abs band">
    <strong>Located at 2240 Fennmoor Avenue, Ste B-3, Santa Rosa, CA 95409</strong>
    <p>In Santa Rosa, when you're a patient of Dr. Kellgren, you can be confident that you're receiving care from the most experienced, knowledgeable, and skilled cosmetic dentist in Sonoma County.</p>
    <p>Dr. Kellgren is an award-winning leader in restorative dentistry and a genial professional. His humor, dedication, and talent ensure you a pleasant experience and superb, long-lasting results.</p>
  </section>

  <aside class="abs promo">
    <h4>We offer an Initial Patient Examination, X-rays and Cleaning for $79.00.</h4>
    <p>**New patients only. Offers are<br>&nbsp;&nbsp;&nbsp;&nbsp;cash patients only.&nbsp; Insurance<br>&nbsp;&nbsp;&nbsp;&nbsp;will be billed at full value.</p>
  </aside>
  <div class="abs rail-rule"></div>

  <div class="abs rail hours">
    <h4 class="rail-title" style="font-weight:400">OFFICE HOURS</h4>
    <b>Our usual office hours are:</b>
    <ul><li>Monday 9 am to 6 pm</li><li>Tuesday 9 am to 5 pm</li><li>Wednesday 9 am to 5 pm</li><li>Thursday 9 am to 5 pm</li><li>Friday 7:30 am to 5 pm</li></ul>
  </div>
  <a class="abs rail rail-title map">MAP TO OFFICE</a>
  <a class="abs rail rail-title stay">WHERE TO STAY?</a>
  <div class="abs rail contact">
    <p>Please contact us at<br><strong>(555) 014-2290.</strong></p>
    <p style="margin-top:17px">To contact us outside office hours for an emergency, please call <strong>(555) 013-7741.</strong></p>
  </div>

  <section class="abs main provides">
    <h2 class="section-title" style="font-weight:400">DR. KELLGREN PROVIDES</h2>
    <ul class="services">
      <li><b>General dentistry</b> - oral hygiene, cavity detection and repair, crowns.</li>
      <li><b>Cosmetic/restorative dentistry</b> - broken or misshapen teeth, crooked smiles, unsightly gaps</li>
      <li><b>Non-metal fillings</b> - nontoxic, durable tooth-colored resin fillings that are proven to provide better results</li>
      <li><b>Tooth shaping</b> - extending, shortening or otherwise reshaping teeth for improved esthetics</li>
      <li><b>Complete smile make-over's</b> - resin veneers that reshape the whole mouth while preserving natural teeth</li>
      <li><b>Tooth whitening</b> - at-home bleaching options to make teeth appear years younger</li>
      <li><b>Laser Dentistry, Sleep Dentistry, and Implant Dentistry with the Finest and Latest Equipment and Materials.</b></li>
      <li><b>Dental Implants to replace missing teeth.</b></li>
      <li><b>Sedation Dentistry so you can be relaxed.</b></li>
    </ul>
  </section>
  <div class="abs divider"></div>

  <section class="abs main commitment">
    <h2 class="section-title" style="font-weight:400">DR. KELLGREN' COMMITMENT</h2>
    <div class="letter">
      <p>After 25 years of teaching dentists how to refine their technique and many years of writing textbooks, I currently devote my time to my office and the hands-on practice of dentistry. I'd like to welcome you personally to my dental practice, and I invite you to meet my highly experienced team of professionals.</p>
      <p>Dr. Kellgren and his Associated have offered complete dental care of the highest quality since 1978. We provide Preventive Services, Tooth Whitening and Cosmetic Dentistry for a beautiful smile, Endodontics (root canal treatment) to treat painful teeth, Sedation Dentistry so you can relax, and Dental Implants to restore what is missing. We offer total care.</p>
      <p class="motto">Our approach to your health is simple: We use our education, experience and dedication to provide every patient with superior dental care.</p>
      <p class="motto">This passion for excellence is not just a goal, but a standard every member of our team holds.</p>
      <p>We also pride ourselves with our state of the art procedures, training and technology. This includes creating a beautiful smile using techniques that preserve as much of the original tooth as possible.</p>
      <p>Our abilities are renowned throughout the dental profession and I hope if you have any questions you will contact us by an e-mail note, by phone or just by dropping by.</p>
      <p>Thank you.</p>
      <p>Sincerely,</p>
      <p>Martin Kellgren, DDS FAGD</p>
    </div>
  </section>
</div>
</body>
</html>
```